Painting Valtoni Renovations New buildings

Paint jobs plasterwork renovations new building customer painter paper drywall Entsorgungen.neukunden win color splash pleasure in colors competent clean fast reliable new try build demolition color combinations color concepts offers washing façade painting wood stains new projects old building renovations yes no beautiful new old sell secure solve paint over paint paint spray paint lye assemble disassemble sell buy trade oil dust new old assembly disassembly putty sanding fashion devastation copying belief feng shui kleopatra pompes beer colors swamp lime abrasion release tighten

Target Market(s)

construction industry

Contact Information for Business Card

Maler

Font styles to use
Serif

Colors
f04a50
959595

Requirements
Must have
• elegant appearance
Nice to have
• simply goal-oriented clientele in detail
Should not have
• too colorful

```html
<!DOCTYPE html>
<html lang="en">
<head>
<meta charset="utf-8">
<title>Lorvano – Business Card</title>
<link href="https://fonts.googleapis.com/css2?family=Poppins:wght@600&family=Questrial&display=swap" rel="stylesheet">
<style>
  :root {
    --backdrop: #2a2926;
    --card: #ffffff;
    --accent: #f04a50;
    --grey: #959595;
    --ink: #333333;
  }
  html, body {
    margin: 0;
    width: 1200px;
    height: 801px;
    overflow: hidden;
    background: var(--backdrop);
  }
  .card {
    position: absolute;
    left: 100px;
    top: 115px;
    width: 1000px;
    height: 572px;
    background: var(--card);
    font-family: "Questrial", "Century Gothic", sans-serif;
    overflow: hidden;
  }
  .brand {
    position: absolute;
    left: 92px;
    top: 92px;
    display: flex;
    align-items: center;
    gap: 14px;
  }
  .brand-dot {
    width: 22px;
    height: 22px;
    border-radius: 50%;
    background: var(--accent);
  }
  .brand-name {
    font-family: "Poppins", sans-serif;
    font-weight: 600;
    font-size: 54px;
    line-height: 1;
    color: var(--accent);
    letter-spacing: 0.5px;
  }
  .divider {
    position: absolute;
    left: 60px;
    top: 208px;
    width: 640px;
    height: 1.5px;
    background: var(--accent);
  }
  .contact {
    position: absolute;
    left: 92px;
    top: 240px;
    color: var(--grey);
    font-size: 25px;
    line-height: 1.28;
  }
  .address { margin: 0 0 14px 0; }
  .contact-list {
    list-style: none;
    margin: 0;
    padding: 0;
  }
  .contact-list li {
    display: flex;
    align-items: center;
    gap: 14px;
    margin-bottom: 4px;
  }
  .contact-list svg {
    width: 17px;
    height: 17px;
    fill: var(--accent);
    flex: none;
  }
  .person {
    position: absolute;
    left: 722px;
    top: 226px;
  }
  .person-name {
    margin: 0;
    font-family: "Poppins", sans-serif;
    font-weight: 600;
    font-size: 32px;
    line-height: 1.1;
    color: var(--accent);
  }
  .person-role {
    margin: 4px 0 0 2px;
    font-size: 22px;
    color: var(--ink);
  }
  .edge-tab {
    position: absolute;
    right: 0;
    top: 304px;
    width: 36px;
    height: 64px;
    background: var(--accent);
  }
</style>
</head>
<body>
  <div class="card">
    <div class="brand">
      <span class="brand-dot"></span>
      <span class="brand-name">Lorvano</span>
    </div>

    <div class="divider"></div>

    <div class="contact">
      <p class="address">4810 Alder Lane, Suite 220<br>Brookfield Park, OH 44207</p>
      <ul class="contact-list">
        <li>
          <svg viewBox="0 0 24 24" aria-hidden="true"><path d="M6.6 10.8a15.1 15.1 0 0 0 6.6 6.6l2.2-2.2c.3-.3.7-.4 1-.2 1.1.4 2.3.6 3.6.6.6 0 1 .4 1 1V20c0 .6-.4 1-1 1A17 17 0 0 1 3 4c0-.6.4-1 1-1h3.5c.6 0 1 .4 1 1 0 1.3.2 2.5.6 3.6.1.3 0 .7-.2 1l-2.3 2.2z"/></svg>
          330-555-0147
        </li>
        <li>
          <svg viewBox="0 0 24 24" aria-hidden="true"><path d="M6 2h12v5H6zM4 8h16a2 2 0 0 1 2 2v7h-4v5H6v-5H2v-7a2 2 0 0 1 2-2zm4 8v4h8v-4z"/></svg>
          330-555-0148
        </li>
        <li>
          <svg viewBox="0 0 24 24" aria-hidden="true"><path d="M2 5h20v14H2zm2 2v.5l8 5.5 8-5.5V7l-8 5.5z"/></svg>
          info@lorvanopainting.com
        </li>
        <li>
          <svg viewBox="0 0 24 24" aria-hidden="true"><path d="M12 2a10 10 0 1 0 0 20 10 10 0 0 0 0-20zm-1 17.9A8 8 0 0 1 4.1 11L9 16v1c0 1.1.9 2 2 2zm6.9-2.5A2 2 0 0 0 16 16h-1v-3c0-.6-.4-1-1-1H8v-2h2c.6 0 1-.4 1-1V7h2a2 2 0 0 0 2-2v-.4a8 8 0 0 1 2.9 12.8z"/></svg>
          www.lorvanopainting.com
        </li>
      </ul>
    </div>

    <div class="person">
      <h1 class="person-name">Merenda Valtoni</h1>
      <p class="person-role">Managing Director</p>
    </div>

    <div class="edge-tab"></div>
  </div>
</body>
</html>
```